indépendant en tant que Massothérapeute et Préparateur Mental, j'ai besoin de ...

Massothérapeute et préparateur mental indépendant, je recherche une carte de visite sobre et dynamique, sans images liées au massage ou à la préparation mentale mais intégrant mon logo. Les couleurs que j'aime bien sont : Blanc, gris, anthracite, noir et jaune

carte de préférence Horizontale
neutre qui puisse toucher le deux domaines Massothérapie et préparation mentale

Requirements
Must have
• mon projet doit intégrer au recto:
LOGO
Loïc Bardemaz
078 315 26 48
info@loicbardemaz-exemple.ch
et éventuellement www.loicbardemaz-exemple.ch

et au verso les deux adresses:

Chemin des Grèvelins 7B
1350 Orbe

Avenue des Mélèzes 9
1630 Bulle

Should not have
• mon projet ne doit pas contenir d'image en liens avec le massage ni la préparation mentale.

```html
<!DOCTYPE html>
<html lang="fr">
<head>
<meta charset="utf-8">
<title>Loïc Bardemaz – Carte de visite</title>
<link rel="stylesheet" href="https://fonts.googleapis.com/css2?family=Arimo:wght@400&family=Montserrat:wght@500;700&display=swap">
<style>
  :root {
    --anthracite: #363636;
    --white: #ffffff;
    --ink: #2e2e2e;
    --accent-grey: #aaaaaa;
    --faint: #e8e8e8;
    --frame: #555555;
  }
  * { margin: 0; padding: 0; box-sizing: border-box; }
  html, body { width: 1010px; height: 1200px; overflow: hidden; background: var(--white); }
  body { position: relative; font-family: "Arimo", Arial, sans-serif; color: var(--ink); }

  .card { position: absolute; left: 47px; width: 917px; height: 539px; }

  /* Front */
  .card--front { top: 32px; background: var(--anthracite); color: var(--white); }
  .brand { position: absolute; left: 0; right: 0; text-align: center; white-space: nowrap; }
  .brand__name {
    top: 296px; font-family: "Montserrat", sans-serif; font-weight: 700;
    font-size: 60px; letter-spacing: 1px; line-height: 1;
  }
  .brand__square {
    display: inline-block; width: 20px; height: 20px; background: var(--white);
    margin-right: 16px; vertical-align: 6px;
  }
  .brand__tagline {
    top: 366px; font-family: "Montserrat", sans-serif; font-weight: 500;
    font-variant: small-caps; font-size: 26.5px; letter-spacing: 1.5px; line-height: 1;
  }

  /* Back */
  .card--back { top: 608px; background: var(--white); border: 1.5px solid var(--frame); overflow: hidden; }
  .contact__bar { position: absolute; left: -1px; top: 42px; width: 21px; height: 116px; background: var(--accent-grey); }
  .contact { position: absolute; left: 39px; top: 48px; line-height: 1; }
  .contact__name { font-size: 42px; margin-bottom: 9px; }
  .contact__line { font-size: 24px; letter-spacing: 1px; margin-bottom: 5px; }

  .watermark-name {
    position: absolute; left: 62px; top: 300px; font-family: "Montserrat", sans-serif;
    font-weight: 700; font-size: 44px; color: var(--faint); line-height: 1; white-space: nowrap;
  }

  .mini-brand { position: absolute; left: 483px; top: 258px; white-space: nowrap; }
  .mini-brand__name {
    font-family: "Montserrat", sans-serif; font-weight: 700; font-size: 32px;
    color: var(--anthracite); line-height: 1; margin-bottom: 8px;
  }
  .mini-brand__square { display: inline-block; width: 12px; height: 12px; background: var(--anthracite); margin-right: 10px; vertical-align: 4px; }
  .mini-brand__tagline {
    font-family: "Montserrat", sans-serif; font-weight: 500; font-variant: small-caps;
    font-size: 15.5px; letter-spacing: 0.8px; color: var(--ink); line-height: 1;
  }

  .address { position: absolute; left: 483px; font-size: 25px; font-style: normal; letter-spacing: 0.5px; line-height: 27px; }
  .address--first { top: 333px; }
  .address--second { top: 413px; }

  .web-band {
    position: absolute; left: 0; right: 0; bottom: 0; height: 46px; background: var(--anthracite);
    color: var(--white); font-size: 25px; letter-spacing: 0.5px; text-align: center; line-height: 46px;
  }
</style>
</head>
<body>
  <section class="card card--front">
    <div class="brand brand__name"><span class="brand__square"></span>Loïc Bardemaz</div>
    <div class="brand brand__tagline">Massothérapeute / Préparateur Mental</div>
  </section>

  <section class="card card--back">
    <div class="contact__bar"></div>
    <div class="contact">
      <div class="contact__name">Loïc Bardemaz</div>
      <div class="contact__line">078 315 26 48</div>
      <div class="contact__line">info@loicbardemaz-exemple.ch</div>
    </div>

    <div class="watermark-name" aria-hidden="true">Loïc Bardemaz</div>

    <div class="mini-brand">
      <div class="mini-brand__name"><span class="mini-brand__square"></span>Loïc Bardemaz</div>
      <div class="mini-brand__tagline">Massothérapeute / Préparateur Mental</div>
    </div>

    <address class="address address--first">Chemin des Grèvelins 7B<br>1350 Orbe</address>
    <address class="address address--second">Avenue des Mélèzes 9<br>1630 Bulle</address>

    <div class="web-band">www.loicbardemaz-exemple.ch</div>
  </section>
</body>
</html>
```